Business Card for By Karel Voss

Looking to have a business card designed for my lifestyle and fitness company. My company offers personal training, online programming and nutrition advice based out of London, United Kingdom.

I'd like to see modern, sleek designs, focusing on black, matte black or matte grey. Design doesn't need to be overly descriptive as this will also be used as a personal business card. I've included my logo.

Please note that my company is no longer called "Fitness by Karel Voss" but instead "By Karel Voss", this is because of my other ventures. Therefore please don't use the "fitness by karel voss" text.

information about my company can be found at www.bykarelvoss.com

Company is also based out of London (United Kingdom) & Sydney (Australia) this could be reflected on the card.

Industry/Entity Type

Business

Contact Information for Business Card

Karel Voss
+44 7382 615027
karel@bykarelvoss.com
www.bykarelvoss.com

Font styles to use
Sans Serif

Requirements
Must have
• All contact details and inclusion of my logo.

```html
<!DOCTYPE html>
<html lang="en">
<head>
<meta charset="utf-8">
<title>By Karel Voss — Business Card</title>
<link href="https://fonts.googleapis.com/css2?family=Arimo:wght@400;700&display=swap" rel="stylesheet">
<style>
  :root {
    --backdrop: #1d1d1d;
    --card-black: #1a1a1a;
    --card-white: #ffffff;
    --ink: #111111;
    --line-light: #e8e8e8;
    --photo-dark: #2a2b2e;
    --photo-mid: #55565a;
    --photo-warm: #8a7a5c;
  }
  * { margin: 0; padding: 0; box-sizing: border-box; }
  html, body {
    width: 1200px; height: 953px; overflow: hidden;
    background: var(--backdrop);
    font-family: "Arimo", Arial, sans-serif;
  }
  .stage { position: relative; width: 1200px; height: 953px; }

  .card {
    position: absolute;
    width: 560px; height: 320px;
    box-shadow: 0 18px 40px rgba(0,0,0,.55);
    overflow: hidden;
  }

  /* Front */
  .card-front {
    left: 90px; top: 110px;
    background: var(--card-black);
  }
  .card-front .frame {
    position: absolute; inset: 12px;
    border: 1px solid var(--line-light);
  }
  .card-front .brand {
    position: absolute; left: 0; right: 0; top: 50%;
    transform: translateY(-50%);
    display: flex; align-items: center; justify-content: center; gap: 16px;
  }
  .mark-square {
    width: 34px; height: 34px; border: 3px solid var(--card-white);
  }
  .brand-name {
    color: var(--card-white);
    font-weight: 700; font-size: 30px; letter-spacing: 3px;
    text-transform: uppercase;
  }

  /* Back */
  .card-back {
    left: 550px; top: 520px;
    background: var(--card-white);
  }
  .card-back .photo {
    position: absolute; left: 0; top: 0; bottom: 0; width: 330px;
    clip-path: polygon(0 0, 100% 0, 92% 100%, 0 100%);
    background:
      radial-gradient(ellipse at 60% 40%, var(--photo-warm) 0%, transparent 45%),
      radial-gradient(ellipse at 30% 55%, var(--photo-mid) 0%, transparent 55%),
      linear-gradient(160deg, #1b1c1f 0%, var(--photo-dark) 50%, #141416 100%);
  }
  .card-back .frame {
    position: absolute; inset: 12px;
    border: 1px solid #c9c9c9;
  }
  .card-back .info {
    position: absolute; left: 338px; top: 62px; right: 20px;
    color: var(--ink);
  }
  .info .brand { display: flex; align-items: center; gap: 10px; margin-bottom: 30px; }
  .info .mark-square { width: 22px; height: 22px; border: 2.5px solid var(--ink); }
  .info .brand-name { color: var(--ink); font-size: 17px; letter-spacing: 1.5px; }
  .contact { list-style: none; font-size: 12.5px; line-height: 2; }
  .contact strong { font-weight: 700; }
</style>
</head>
<body>
<main class="stage">
  <section class="card card-front" aria-label="Card front">
    <div class="frame"></div>
    <div class="brand">
      <span class="mark-square" aria-hidden="true"></span>
      <span class="brand-name">Karel Voss</span>
    </div>
  </section>

  <section class="card card-back" aria-label="Card back">
    <div class="photo" role="img" aria-label="Photo of athletes doing push-ups in a dark gym"></div>
    <div class="frame"></div>
    <div class="info">
      <div class="brand">
        <span class="mark-square" aria-hidden="true"></span>
        <span class="brand-name">Karel Voss</span>
      </div>
      <ul class="contact">
        <li><strong>Phone:</strong> +44 7382 615027</li>
        <li><strong>Email:</strong> karel@bykarelvoss.com</li>
        <li><strong>Web:</strong> www.bykarelvoss.com</li>
      </ul>
    </div>
  </section>
</main>
</body>
</html>
```